Kleine Website f. Unternehmensdarstellung
Zielgruppe
Geschäftsführer, Marketing & Sales Manager asiatischer Konzerne.
Aufgabenstellung
Wir sind eine Consulting und Handelsagentur mit überwiegend internationaler Kundschaft (Asien 70%).
Für einen Webauftritt, ca. 8 Seiten, haben wir eine Powerpoint Vorlage erstellt, diese zeigt nur die Inhalte. Wir benötigen nun daraus eine Website, haben eigenen Webspace, eigener Server bei Hostquelle. Wir stellen uns als Hintergrundbild auf der Frontpage Hongkong vor. Keine Flash videos oder audio einbindung ! Sprache Englisch, die Texte sollten von uns leicht editierbar sein, falls mal Anpassungen gemacht werden müssen.

```html
<!DOCTYPE html>
<html lang="en">
<head>
<meta charset="utf-8">
<title>Marvessa Group – Agency</title>
<link rel="stylesheet" href="https://fonts.googleapis.com/css2?family=Hind:wght@400;600&display=swap">
<style>
  :root {
    --ink-white: #ffffff;
    --ink-dark: #111111;
    --ink-muted: #8a8a8a;
    --night-top: #0c0d12;
    --night-mid: #2a2730;
    --city-glow: #6b6670;
    --harbour: #141218;
    --panel-bg: rgba(232, 232, 234, 0.78);
  }
  * { margin: 0; padding: 0; box-sizing: border-box; }
  html, body { width: 1200px; height: 696px; overflow: hidden; background: var(--night-top); }
  body { font-family: "Hind", "Trebuchet MS", sans-serif; position: relative; }

  .skyline-backdrop {
    position: absolute; inset: 0;
    background:
      radial-gradient(ellipse 260px 420px at 930px 330px, rgba(255,255,255,0.35), transparent 70%),
      radial-gradient(ellipse 300px 200px at 150px 360px, rgba(220,230,255,0.22), transparent 70%),
      linear-gradient(to bottom, var(--night-top) 0%, var(--night-mid) 38%, var(--city-glow) 62%, var(--night-mid) 78%, var(--harbour) 88%, var(--night-top) 100%);
  }

  .site-header {
    position: absolute; top: 14px; left: 198px; width: 804px;
    display: flex; justify-content: space-between; align-items: center;
  }
  .welcome { color: var(--ink-white); font-size: 20px; font-weight: 400; }
  .brand { display: flex; align-items: center; gap: 10px; color: var(--ink-white); font-size: 30px; font-weight: 600; letter-spacing: 4px; }
  .brand-mark { width: 22px; height: 22px; background: var(--ink-white); }

  .intro {
    position: absolute; top: 76px; left: 0; width: 1200px; text-align: center;
    color: var(--ink-white); font-size: 19px;
  }

  .content-panel {
    position: absolute; top: 120px; left: 198px; width: 804px; height: 422px;
    background: var(--panel-bg); border-radius: 5px;
    padding: 26px 32px; color: var(--ink-dark);
  }
  .content-panel h1 { font-size: 21px; font-weight: 600; margin-bottom: 6px; }
  .content-panel p { font-size: 15px; line-height: 20px; }
  .content-panel p + p { margin-top: 22px; }
  .product-list { list-style: none; margin-top: 18px; font-size: 15px; }
  .product-list li { position: relative; padding-left: 16px; line-height: 26px; }
  .product-list li::before {
    content: ""; position: absolute; left: 2px; top: 10px;
    width: 7px; height: 7px; border-radius: 50%; background: #444;
  }
  .content-panel .call-to-action { margin-top: 22px; }

  .site-footer { position: absolute; top: 638px; left: 0; width: 1200px; text-align: center; }
  .footer-nav { display: flex; justify-content: center; gap: 28px; font-size: 10px; }
  .footer-nav a { color: var(--ink-muted); text-decoration: none; }
  .copyright { margin-top: 5px; font-size: 9.5px; color: var(--ink-muted); }
</style>
</head>
<body>
  <div class="skyline-backdrop" role="img" aria-label="Night skyline of Hong Kong harbour with illuminated towers and searchlights"></div>

  <header class="site-header">
    <div class="welcome">Welcome to the Marvessa Group...</div>
    <div class="brand"><span class="brand-mark"></span>MARVESSA</div>
  </header>

  <div class="intro">Our business segments cover quite an area, please select your piont of interest :</div>

  <main class="content-panel">
    <h1>Agency</h1>
    <p>Agency business means basically we buy products, either OEM or branded, and resell them in our markets through our sales network. We cover Europe (West&amp;East) and Scandinavia as well.</p>
    <p>Currently we are looking for following products or services :</p>
    <ul class="product-list">
      <li>DPSS Lasermodule (from entertainment to laser marking)</li>
      <li>InGaAs Photodioden (chips &amp; assembled) for telcom and avionics</li>
      <li>High Power LEDs (chips &amp; assembled) for automotive, indoor and outdoor lighting</li>
    </ul>
    <p class="call-to-action">If you feel you have a unique product combined with strong USPs, please contact us</p>
  </main>

  <footer class="site-footer">
    <nav class="footer-nav">
      <a href="#">Home</a>
      <a href="#">Agency</a>
      <a href="#">Consultancy</a>
      <a href="#">Technology Finance</a>
      <a href="#">Troubleshooting</a>
      <a href="#">M&amp;A Silent Service</a>
    </nav>
    <div class="copyright">Copyright 2010. Marvessa Group. All Rights Reserved.</div>
  </footer>
</body>
</html>
```